Business Card Design

We are a residential half way house for the addict ,the alcoholic and dual diagnosed in recovery.
i house both men and woman age 18+

Industry/Entity Type

Residential

```html
<!DOCTYPE html>
<html lang="en">
<head>
<meta charset="UTF-8">
<title>Harborlight Family Sober House – Business Card</title>
<link rel="stylesheet" href="https://fonts.googleapis.com/css2?family=Arimo:wght@400;700&family=Open+Sans:wght@300;400&display=swap">
<style>
  :root {
    --backdrop: #e4e4e4;
    --card: #fbfbfb;
    --band: #3a3a3a;
    --ink: #3c3c3c;
    --ink-soft: #555555;
    --mark: #b9b9b9;
  }
  * { box-sizing: border-box; margin: 0; padding: 0; }
  html, body {
    width: 1200px;
    height: 1200px;
    overflow: hidden;
    background: var(--backdrop);
  }
  .canvas {
    position: relative;
    width: 1200px;
    height: 1200px;
    display: flex;
    align-items: center;
    justify-content: center;
  }
  .business-card {
    position: relative;
    width: 1050px;
    height: 600px;
    background: var(--card);
    overflow: hidden;
  }
  .edge-band {
    position: absolute;
    left: 0;
    width: 100%;
    height: 22px;
    background: var(--band);
  }
  .edge-band--top { top: 0; }
  .edge-band--bottom { bottom: 0; }

  .brand {
    position: absolute;
    left: 42px;
    top: 70px;
    display: flex;
    align-items: center;
    gap: 14px;
  }
  .brand__dot {
    width: 34px;
    height: 34px;
    border-radius: 50%;
    background: var(--mark);
  }
  .brand__name {
    font-family: "Open Sans", sans-serif;
    font-weight: 300;
    font-size: 40px;
    color: var(--ink);
    letter-spacing: 0.2px;
  }

  .brand-motif {
    position: absolute;
    left: 445px;
    top: 185px;
    width: 230px;
    height: 230px;
    border-radius: 50%;
    background: radial-gradient(circle, #ececec 0%, #d2d2d2 100%);
  }

  .address {
    position: absolute;
    left: 700px;
    top: 205px;
    font-family: "Arimo", sans-serif;
    font-size: 26px;
    line-height: 1.3;
    color: var(--ink);
    font-style: normal;
  }

  .contact {
    position: absolute;
    left: 72px;
    top: 355px;
    font-family: "Arimo", sans-serif;
    font-size: 26px;
    line-height: 1.32;
    color: var(--ink-soft);
  }
  .contact__tab {
    position: absolute;
    left: 32px;
    top: 360px;
    width: 20px;
    height: 34px;
    background: var(--band);
  }
  .contact__name {
    font-weight: 700;
    color: var(--ink);
  }
  .contact__role { font-size: 24px; }
</style>
</head>
<body>
  <main class="canvas">
    <article class="business-card">
      <div class="edge-band edge-band--top"></div>

      <header class="brand">
        <span class="brand__dot"></span>
        <h1 class="brand__name">Harborlight Family Sober House Inc</h1>
      </header>

      <div class="brand-motif" role="img" aria-label="Large soft brand emblem decoration"></div>

      <address class="address">
        1208 Palmetto Ln<br>
        Seabrook<br>
        Fla 33400
      </address>

      <span class="contact__tab"></span>
      <section class="contact">
        <p class="contact__name">Dana Whitfield</p>
        <p class="contact__role">Owner</p>
        <p>555-014-2718</p>
        <p>555-014-2719</p>
        <p>555-019-4072</p>
        <p>dwhitfield@example.com</p>
      </section>

      <div class="edge-band edge-band--bottom"></div>
    </article>
  </main>
</body>
</html>
```